Business Card and Stationary for Maplecrest Baptist Day School
Maplecrest Baptist Day School
Business Card and Stationary for Maplecrest Baptist Day School - Childcare
Creative Brief
Bright & Fun-filled
Delia Fenwick
Day School Director
4817 W. Tollbridge Rd Hampton, VA 23671
dayschool@maplecrestbaptistexample.com
www.MCDaySchool-example.com
Walking in Faith, Growing Hearts, Nurturing Spirits (See uploaded logo) Theme Verse is: Luke 2:52 And Jesus increased in wisdom and stature, and in favour with God and man.
Hours of Operation: Monday - Friday 6am - 6pm See attached QR Code

```html
<!DOCTYPE html>
<html lang="en">
<head>
<meta charset="utf-8">
<title>Delia Fenwick – Maplecrest Baptist Day School</title>
<link rel="stylesheet" href="https://fonts.googleapis.com/css2?family=Tenor+Sans&family=Josefin+Sans:wght@400;600&family=Raleway:wght@400;500&display=swap">
<style>
  :root {
    --page: #f1f1f1;
    --card: #5c5c5e;
    --card-edge: #505052;
    --emboss-light: #6c6c6e;
    --emboss-dark: #4a4a4c;
    --name: #3b3b3d;
    --light-text: #ececec;
    --muted-text: #d6d6d6;
    --icon: #e4e4e4;
  }
  html, body {
    margin: 0;
    width: 1200px;
    height: 802px;
    overflow: hidden;
    background: var(--page);
  }
  .business-card {
    position: absolute;
    left: 75px;
    top: 101px;
    width: 1050px;
    height: 600px;
    background: linear-gradient(160deg, #646466 0%, var(--card) 55%, var(--card-edge) 100%);
    border-radius: 14px;
    box-shadow: 0 10px 30px rgba(0,0,0,0.18);
    overflow: hidden;
  }
  .emboss-illustration {
    position: absolute;
    left: 0;
    top: 0;
    width: 300px;
    height: 600px;
    background: radial-gradient(ellipse at 40% 55%, var(--emboss-light) 0%, var(--emboss-dark) 70%, var(--card) 100%);
    opacity: 0.85;
  }
  .identity {
    position: absolute;
    left: 360px;
    right: 70px;
    top: 150px;
    text-align: right;
  }
  .school-name {
    font-family: "Josefin Sans", sans-serif;
    font-weight: 600;
    font-size: 17px;
    letter-spacing: 1px;
    color: var(--light-text);
    margin: 0 0 14px;
  }
  .person-name {
    font-family: "Tenor Sans", sans-serif;
    font-size: 54px;
    color: var(--name);
    margin: 0;
    line-height: 1;
    text-shadow: 0 1px 0 rgba(255,255,255,0.18), 0 -1px 0 rgba(0,0,0,0.35);
  }
  .person-title {
    font-family: "Josefin Sans", sans-serif;
    font-weight: 400;
    font-size: 22px;
    letter-spacing: 6px;
    text-transform: uppercase;
    color: var(--light-text);
    margin: 10px 0 0;
  }
  .contact-list {
    position: absolute;
    left: 395px;
    top: 370px;
    margin: 0;
    padding: 0;
    list-style: none;
    font-family: "Raleway", sans-serif;
    font-size: 19px;
    color: var(--muted-text);
  }
  .contact-list li {
    display: flex;
    align-items: center;
    height: 34px;
  }
  .contact-list .address {
    margin-bottom: 8px;
  }
  .contact-icon {
    width: 20px;
    height: 20px;
    margin-right: 14px;
    flex: none;
  }
</style>
</head>
<body>
  <article class="business-card">
    <div class="emboss-illustration" role="img" aria-label="Embossed illustration of a church with a cross and a group of children"></div>

    <header class="identity">
      <p class="school-name">Maplecrest Baptist Day School</p>
      <h1 class="person-name">Delia Fenwick</h1>
      <p class="person-title">Day School Director</p>
    </header>

    <ul class="contact-list">
      <li class="address">4817 W. Tollbridge Rd Hampton, VA 23671</li>
      <li>
        <svg class="contact-icon" viewBox="0 0 20 20" aria-hidden="true">
          <rect width="20" height="20" rx="3" fill="var(--icon)"/>
          <path d="M6 4.5h2.5l1 3-1.5 1.2a8 8 0 0 0 3.3 3.3l1.2-1.5 3 1V14a1.5 1.5 0 0 1-1.5 1.5A10 10 0 0 1 4.5 6 1.5 1.5 0 0 1 6 4.5z" fill="var(--card)"/>
        </svg>
        757 555 0142
      </li>
      <li>
        <svg class="contact-icon" viewBox="0 0 20 20" aria-hidden="true">
          <rect width="20" height="20" rx="3" fill="var(--icon)"/>
          <rect x="5" y="8" width="10" height="7" rx="1" fill="var(--card)"/>
          <rect x="7" y="4" width="6" height="4" fill="var(--card)"/>
        </svg>
        757 555 0143
      </li>
      <li>
        <svg class="contact-icon" viewBox="0 0 20 20" aria-hidden="true">
          <rect width="20" height="20" rx="3" fill="var(--icon)"/>
          <rect x="4" y="6" width="12" height="8" rx="1" fill="none" stroke="var(--card)" stroke-width="1.6"/>
          <path d="M4.5 6.5 10 11l5.5-4.5" fill="none" stroke="var(--card)" stroke-width="1.6"/>
        </svg>
        dayschool@maplecrestbaptistexample.com
      </li>
      <li>
        <svg class="contact-icon" viewBox="0 0 20 20" aria-hidden="true">
          <rect width="20" height="20" rx="3" fill="var(--icon)"/>
          <circle cx="10" cy="10" r="5.5" fill="none" stroke="var(--card)" stroke-width="1.5"/>
          <path d="M4.5 10h11M10 4.5c-2.5 3-2.5 8 0 11M10 4.5c2.5 3 2.5 8 0 11" fill="none" stroke="var(--card)" stroke-width="1.2"/>
        </svg>
        www.MCDaySchool-example.com
      </li>
    </ul>
  </article>
</body>
</html>
```